Dog care service needs advertising poster

Our company is Pawfield Haven. We provide care for dogs while their owners are away, either through home visits or a holiday stay in the homes of carefully selected minders. Our existing website & Facebook cover should provide all the colour cues for a poster - namely blues, blondes and grey. We have an existing logo (provided). We can feature the same imagery from our website as I have purchased the rights to the stock images.

www.pawfieldhaven.com.au
www.facebook.com/pawfieldhavenau

This brief is for design of a poster that can be placed in vet surgeries, groomers, on community noticeboards. It should be scalable to print in three sizes, A5, A4 & A3.

We wish to clearly communicate our three areas of service "dog minding, home visits, dog walking".

We would like to have the files ready for upload to Printlorra (or similar) for immediate printing.

Target Market(s)

Dog owners who love their dogs like family.

Industry/Entity Type

Advertising

Font styles to use
Sans Serif

Colors
33a6d7
3276b5

Requirements
Must have
• Logo
• www.pawfieldhaven.com.au
• Telephone number
• Three services - Dog Minding, Home Visits, Dog Walking
Nice to have
• use of our existing stock photography to highlight the three areas of service - Dog minding, home visits, dog walking. Existing colour palette - blues, blondes and grey.
• Text that can be used:
• Western Sydney’s complete dog care service.
• Dog Minding - Your dog stays in the home of one of our carefully selected minders.Treated like part of the family, they enjoy all the creature comforts they are used to.
• Home Visits - We visit your dog at your home for feeding, walking and playtime. Short of long visits available.
• Dog Walking - If you can't walk your dog for any reason we are here to help. 1/2 hour or hourly walks available.
• Contact us today for a tailored package to meet your needs.
Should not have
• Any additional illustrations beyond the logo.

```html
<!DOCTYPE html>
<html lang="en">
<head>
<meta charset="utf-8">
<title>Pawfield Haven – Dog Care Poster</title>
<link href="https://fonts.googleapis.com/css2?family=Montserrat:wght@400;500;600;700&family=Open+Sans:wght@600;700&display=swap" rel="stylesheet">
<style>
  :root {
    --sky-blue: #33a6d7;
    --tab-blue: #5bbbe6;
    --royal-blue: #3276b5;
    --tab-royal: #3a7fc0;
    --slate: #3e4656;
    --slate-tab: #555d6b;
    --fold-sky: #2a8fbd;
    --fold-royal: #285f96;
    --fold-slate: #2e3441;
    --footer-grey: #7b7b7b;
    --footer-dark: #6a6a6a;
    --logo-ink: #2d4f7a;
    --white: #ffffff;
  }
  * { margin: 0; padding: 0; box-sizing: border-box; }
  html, body { width: 849px; height: 1200px; overflow: hidden; background: var(--white); }
  .poster {
    position: relative; width: 849px; height: 1200px; overflow: hidden;
    font-family: "Open Sans", Arial, sans-serif; color: var(--white); background: var(--white);
  }
  .display { font-family: "Montserrat", Arial, sans-serif; }

  .hero-photo {
    position: absolute; left: 0; top: 0; width: 849px; height: 370px;
    background:
      radial-gradient(ellipse 190px 210px at 715px 150px, #d2a260 0%, #b07e42 50%, rgba(140,100,55,0) 78%),
      linear-gradient(100deg, rgba(0,0,0,0) 57%, #4a6788 61%, #2f4662 72%, #222e3d 100%),
      linear-gradient(180deg, #e4edf3 0px, #cdd8de 55px, rgba(205,210,210,0) 90px),
      linear-gradient(180deg, #c7c6c1 0%, #a9a49c 45%, #8f8a83 100%);
  }
  .logo-panel {
    position: absolute; left: 30px; top: 18px; width: 355px; height: 102px;
    background: rgba(255,255,255,0.85);
    display: flex; align-items: center; gap: 16px; padding-left: 34px;
  }
  .logo-mark { width: 44px; height: 44px; border-radius: 50%; background: var(--logo-ink); flex: none; }
  .logo-name { font-family: "Open Sans", Arial, sans-serif; font-weight: 700; font-size: 29px; line-height: 1.05; color: var(--logo-ink); }

  .tagline {
    position: absolute; left: 30px; top: 192px; width: 405px; height: 83px;
    background: rgba(60,60,60,0.55); text-align: center; padding-top: 9px;
  }
  .tagline-lead { font-weight: 700; font-size: 28px; letter-spacing: 2px; line-height: 1.2; }
  .tagline-sub { font-weight: 400; font-size: 21.5px; letter-spacing: 0.6px; line-height: 1.45; }

  .services-title {
    position: absolute; left: 444px; top: 320px; font-weight: 600; font-size: 44px;
    letter-spacing: 15px; line-height: 1; text-shadow: 0 1px 3px rgba(0,0,0,0.35);
  }
  .folds { position: absolute; left: 0; top: 0; }

  .service-copy {
    position: absolute; left: 0; padding-left: 32px;
    font-weight: 600; font-size: 22.5px; line-height: 31.5px;
  }
  .service-copy .line { display: block; white-space: nowrap; }
  .service-copy.justified .line { text-align: justify; text-align-last: justify; }
  .service-copy.justified .line:last-child { text-align-last: left; }
  .service-copy.minding { top: 352px; width: 398px; height: 220px; background: var(--sky-blue); padding-top: 17px; }
  .service-copy.minding .line { width: 335px; }
  .service-copy.visits { top: 592px; width: 388px; height: 220px; background: var(--royal-blue); padding-top: 43px; }
  .service-copy.visits .line { width: 326px; }
  .service-copy.walking { top: 835px; width: 378px; height: 222px; background: var(--slate); padding-top: 36px; font-size: 21.5px; }

  .service-photo { position: absolute; }
  .service-photo.minding { left: 440px; top: 382px; width: 317px; height: 223px;
    background: linear-gradient(180deg, #e2eef4 0%, #c4dfa0 35%, #8cbf55 60%, #4f8d27 100%); }
  .service-photo.visits { left: 430px; top: 622px; width: 327px; height: 225px;
    background: linear-gradient(180deg, #f6f4f0 0%, #ebe7e0 36%, #b89068 46%, #8e6840 70%, #a07a50 100%); }
  .service-photo.walking { left: 418px; top: 865px; width: 339px; height: 225px;
    background: linear-gradient(180deg, #3e5a2c 0%, #6b8448 40%, #5fa23e 62%, #3c8c2a 100%); }

  .service-tab {
    position: absolute; left: 760px; width: 89px; display: flex; align-items: center; justify-content: center;
    writing-mode: vertical-rl; font-weight: 600; font-size: 30px; letter-spacing: 0.5px;
  }
  .service-tab.minding { top: 382px; height: 223px; background: var(--tab-blue); }
  .service-tab.visits { top: 622px; height: 225px; background: var(--tab-royal); }
  .service-tab.walking { top: 865px; height: 225px; background: var(--slate-tab); }

  .contact-block {
    position: absolute; left: 0; top: 1080px; width: 363px; height: 86px;
    background: var(--footer-grey); text-align: center; padding-top: 10px;
  }
  .contact-web { font-size: 19px; font-weight: 500; line-height: 1.3; }
  .contact-phone { font-size: 25px; font-weight: 600; letter-spacing: 1.5px; line-height: 1.55; white-space: pre; }

  .call-to-action {
    position: absolute; left: 412px; top: 1112px; width: 437px; height: 88px;
    background: var(--footer-dark); padding: 9px 14px 0 13px;
    font-weight: 700; font-size: 21.5px; line-height: 34px;
  }
  .call-to-action .line { display: block; white-space: nowrap; text-align: justify; text-align-last: justify; }
</style>
</head>
<body>
<div class="poster">
  <div class="hero-photo" role="img" aria-label="Photo of a golden retriever puppy leaning out of a car window at the beach"></div>

  <div class="logo-panel">
    <span class="logo-mark"></span>
    <span class="logo-name">Pawfield Haven</span>
  </div>

  <div class="tagline display">
    <div class="tagline-lead">Western Sydney’s</div>
    <div class="tagline-sub">complete dog care service</div>
  </div>

  <svg class="folds" width="849" height="1200" viewBox="0 0 849 1200" aria-hidden="true">
    <polygon points="340,338 849,338 849,352 398,352" fill="#ececec"/>
    <polygon points="398,352 849,352 849,370 435,382 435,382" fill="#ffffff"/>
    <polygon points="398,352 435,382 435,605 398,572" fill="var(--fold-sky)"/>
    <polygon points="388,592 425,622 425,847 388,812" fill="var(--fold-royal)"/>
    <polygon points="378,835 413,865 413,1090 378,1057" fill="var(--fold-slate)"/>
    <polygon points="363,1080 412,1112 412,1200 363,1166" fill="#d4d4d4"/>
  </svg>

  <div class="services-title display">SERVICES</div>

  <div class="service-copy minding justified">
    <span class="line">Your dog stays in the home of</span>
    <span class="line">one of our carefully selected</span>
    <span class="line">minders. Treated like part of</span>
    <span class="line">the family, they enjoy all the</span>
    <span class="line">creature comforts they are</span>
    <span class="line">used to.</span>
  </div>
  <div class="service-photo minding" role="img" aria-label="Photo of a dog lying in green grass"></div>
  <div class="service-tab minding">Dog Minding</div>

  <div class="service-copy visits justified">
    <span class="line">We visit your dog at your</span>
    <span class="line">home for feeding, walking</span>
    <span class="line">and playtime. Short of long</span>
    <span class="line">visits available.</span>
  </div>
  <div class="service-photo visits" role="img" aria-label="Photo of a small dog sitting on a doormat reading HOME"></div>
  <div class="service-tab visits">Home Visits</div>

  <div class="service-copy walking">
    <span class="line">If you can't walk your dog</span>
    <span class="line">for any reason we are here</span>
    <span class="line">to help. 1/2 hour or hourly</span>
    <span class="line">walks available.</span>
  </div>
  <div class="service-photo walking" role="img" aria-label="Photo of a bulldog on a lead walking on grass"></div>
  <div class="service-tab walking">Dog Walking</div>

  <div class="contact-block display">
    <div class="contact-web">www.pawfieldhaven.com.au</div>
    <div class="contact-phone">Phone:  0400 555 018</div>
  </div>

  <div class="call-to-action display">
    <span class="line">Contact us today for a tailored</span>
    <span class="line">package to meet your needs</span>
  </div>
</div>
</body>
</html>
```